BUSINESS CARD - HALVERDINE RURAL SERVICES

I would like to create a business card for my fertilizer spreading business. I would like to incorporate my existing logo and also a description of the services offered. The business card will be given to farmers so must be kept simple but effective. It will also be left in stores so much also be eye catching in order to stand out from other cards.

Target Market(s)

FARMERS

Requirements
Must have
• FRONT OF CARD = EXISTING LOGO + "CUSTOMISED SPREADING" below the logo

REAR Of CARD = SERVICES OFFERED AND CONTACT DETAILS

- Bulk fertilizer including Lime, Gypsum, Manure & Compost
- Granular fertilizer including Single Super, Urea, Gran-am, & Custom Blends
- Modern equipment - Autosteer & Variable Rate Capable
- Friendly & Reliable Service
- Contact Gus: 0471 502 318
Nice to have
• utilize same color scheme as existing logo

```html
<!DOCTYPE html>
<html lang="en">
<head>
<meta charset="utf-8">
<title>Halverdine Rural Services – Business Card</title>
<link href="https://fonts.googleapis.com/css2?family=Poppins:wght@400;500;600;700;800&display=swap" rel="stylesheet">
<style>
  :root {
    --backdrop: #1f1f23;
    --card-white: #ffffff;
    --charcoal: #4a4a4c;
    --charcoal-dark: #3d3d3f;
    --orange: #f39322;
    --ink: #3a3a3c;
  }
  * { box-sizing: border-box; margin: 0; padding: 0; }
  html, body { width: 1200px; height: 800px; overflow: hidden; }
  body {
    background: var(--backdrop);
    font-family: "Poppins", sans-serif;
    display: flex;
    align-items: center;
    justify-content: center;
    gap: 40px;
  }
  .card {
    position: relative;
    width: 540px;
    height: 310px;
    background: var(--card-white);
    border-radius: 18px;
    overflow: hidden;
  }
  .card svg.card-shapes { position: absolute; inset: 0; }

  /* Rear card */
  .brand-circle {
    position: absolute;
    left: 38px; top: 62px;
    width: 190px; height: 190px;
    display: flex; flex-direction: column; align-items: center; justify-content: center;
    text-align: center;
  }
  .brand-circle .name {
    font-weight: 700;
    font-size: 17px;
    line-height: 1.15;
    color: var(--charcoal);
  }
  .service-list {
    position: absolute;
    left: 240px; top: 42px;
    width: 290px;
    list-style: none;
  }
  .service-list li {
    position: relative;
    height: 52px;
    padding-left: 18px;
    display: flex; align-items: center;
    color: #fff;
    font-size: 10.5px;
    line-height: 1.35;
  }
  .service-list li::before {
    content: "";
    position: absolute; left: 2px; top: 50%;
    width: 7px; height: 7px; margin-top: -3.5px;
    border-radius: 50%;
    background: var(--orange);
  }
  .contact {
    position: absolute;
    left: 240px; bottom: 26px;
    display: flex; align-items: center; gap: 8px;
    font-size: 15px; font-weight: 600;
    color: var(--ink);
  }
  .contact svg { width: 16px; height: 16px; }

  /* Front card */
  .front-brand {
    position: absolute;
    left: 60px; top: 70px;
    display: flex; align-items: center; gap: 16px;
  }
  .front-brand .mark {
    width: 64px; height: 64px; border-radius: 50%;
    border: 6px solid var(--charcoal);
  }
  .front-brand .name {
    font-weight: 800;
    font-size: 30px;
    line-height: 1.05;
    color: var(--charcoal);
  }
  .tagline {
    position: absolute;
    left: 232px; top: 240px;
    color: #fff;
    font-size: 21px;
    font-weight: 600;
    line-height: 1;
    white-space: nowrap;
    transform: rotate(-17deg);
    transform-origin: left top;
  }
</style>
</head>
<body>

  <section class="card card-rear">
    <svg class="card-shapes" viewBox="0 0 540 310" aria-hidden="true">
      <rect class="service-panel" x="210" y="40" width="330" height="210" fill="var(--charcoal)"/>
      <rect x="210" y="91" width="330" height="2" fill="#fff"/>
      <rect x="210" y="144" width="330" height="2" fill="#fff"/>
      <rect x="210" y="197" width="330" height="2" fill="#fff"/>
      <circle cx="133" cy="157" r="118" fill="#fff"/>
      <circle cx="133" cy="157" r="92" fill="none" stroke="var(--charcoal)" stroke-width="8"/>
    </svg>
    <div class="brand-circle">
      <span class="name">Halverdine<br>Rural<br>Services</span>
    </div>
    <ul class="service-list">
      <li>Bulk fertilizer including Lime,<br>Gypsum, Manure &amp; Composts</li>
      <li>Granular fertilizer including Single Super,<br>Urea, Gran-am, &amp; Custom Blends</li>
      <li>Modern equipment</li>
      <li>Friendly &amp; Reliable Service</li>
    </ul>
    <div class="contact">
      <svg viewBox="0 0 24 24" aria-hidden="true"><path fill="var(--orange)" d="M6.6 10.8a15.1 15.1 0 0 0 6.6 6.6l2.2-2.2a1 1 0 0 1 1-.25 11.4 11.4 0 0 0 3.6.57 1 1 0 0 1 1 1V20a1 1 0 0 1-1 1A17 17 0 0 1 3 4a1 1 0 0 1 1-1h3.5a1 1 0 0 1 1 1c0 1.25.2 2.45.57 3.57a1 1 0 0 1-.25 1z"/></svg>
      <span>Contact Gus: 0471 502 318</span>
    </div>
  </section>

  <section class="card card-front">
    <svg class="card-shapes" viewBox="0 0 540 310" aria-hidden="true">
      <path class="swoosh" d="M0 310 L0 262 C180 250 380 200 470 110 C500 80 520 40 540 20 L540 310 Z" fill="var(--charcoal)"/>
      <path d="M540 0 C520 30 500 60 470 60 C500 40 505 20 500 0 Z" fill="#fff"/>
      <path d="M455 140 C430 110 440 60 490 10 C470 50 460 90 475 120 Z" fill="var(--orange)"/>
      <path d="M500 150 C490 110 505 70 540 40 L540 120 C525 130 510 140 500 150 Z" fill="#fff"/>
    </svg>
    <div class="front-brand">
      <span class="mark"></span>
      <span class="name">Halverdine<br>Rural Services</span>
    </div>
    <p class="tagline">Customised Spreading</p>
  </section>

</body>
</html>
```